Design for company homepage promoting to the pharmaceutical industry

Our company produces medical education materials and services for the pharmaceutical industry. Our existing website (www.quorvane.net.au) provides more information.
 
We need a homepage design for our new company website we are creating. Our site will not have a great amount of content, we want it to be fast, user friendly and easily adaptable to viewing on any platform, and through any browser. We don't want it over-designed - i.e. no highly animated banner flags, backgrounds, obscure webfonts, too many graphics etc. Attached are files indicating our existing company logo and design. We want the logo and rings to be retained. We've also attached draft copy for the website.
The final website may be designed in Wordpress (still to be confirmed)
 
This is a design to replace the current site (www.quorvane.net.au). Content will also be revised.
Things we don't like about our current design - doesn't use our current branding, is not very exciting, old fashioned 'standard' format, too much content, just doesn't look that good, boring.
 
Examples of sites we like:
www.bralimo.com.au
http://factsheets.tenvoramed.com.au/index.html
 
Features we like from these sites - fast, responsive, short and to the point, cross-platform compatible including smartphones, and looks good
 
Main reasons people will visit our site: to find out whether we can provide services they might be looking for, to make a decision on whether they are interested in what we offer so they can get in touch with us, and to get our contact details.
Main thing we want to achieve from website visits is that it looks good enough and provides enough summary information on us so that they want to get in touch with us, to offer us work or to ask us to come in and meet them to provide more info on what we do.
Two most important calls to action from our website
· make the decision that we can do what you are looking for
· get in touch with us.
Updates

Thanks everyone for your submissions. At this stage with the Christmas break upon us, we are yet to finalise our decision, and will make a decision early in the new year. I hope everyone has a good holiday break.
Kind regards
Giles

Target Market(s)

Pharmaceutical industry professionals, marketers and medical professionals.

Industry/Entity Type

Pharmaceutical

Requirements
Must have
• Company logo and rings must be incorporated, company colour - blue - must be in there.
Should not have
• Complex animation or graphics that will slow the upload or limit cross-platform compatability/viewing on smartphones etc.

```html
<!DOCTYPE html>
<html lang="en">
<head>
<meta charset="utf-8">
<title>Quorvane — Healthcare Communication Specialists</title>
<link rel="stylesheet" href="https://fonts.googleapis.com/css2?family=Open+Sans:wght@400;600;700&family=Roboto+Slab:wght@300;400&display=swap">
<style>
  :root {
    --brand-blue: #3bbde9;
    --brand-blue-text: #29a9dc;
    --page-grey: #e2e2e2;
    --footer-grey: #f2f2f2;
    --card-border: #e3e3e3;
    --rule: #dcdcdc;
    --ink: #222222;
    --body-text: #666666;
    --white: #ffffff;
  }
  * { box-sizing: border-box; margin: 0; padding: 0; }
  html, body { width: 964px; height: 1200px; overflow: hidden; }
  body {
    background: var(--page-grey);
    font-family: "Open Sans", Arial, sans-serif;
    color: var(--ink);
    position: relative;
  }
  .page {
    position: absolute;
    left: 24px; top: 0;
    width: 916px; height: 1200px;
    background: var(--white);
  }
  .site-header {
    position: absolute; left: 0; top: 0;
    width: 916px; height: 64px;
    background: var(--brand-blue);
  }
  .brand {
    position: absolute; left: 104px; top: 10px;
    font-family: "Roboto Slab", Georgia, serif;
    font-weight: 400;
    font-size: 34px;
    line-height: 40px;
    color: var(--white);
    letter-spacing: -0.5px;
  }
  .main-nav { position: absolute; top: 0; left: 0; height: 64px; }
  .main-nav a {
    position: absolute; top: 23px;
    font-size: 12px; color: var(--white);
    text-decoration: none; white-space: nowrap;
  }
  .main-nav a.is-current { font-weight: 700; }
  .search-icon { position: absolute; left: 803px; top: 25px; }

  .hero {
    position: absolute; left: 0; top: 64px;
    width: 916px; height: 548px;
    background: linear-gradient(100deg, #eef0f2 0%, #e4e6ea 40%, #dfe2e8 65%, #eceff2 100%);
  }

  .services { position: absolute; left: 101px; top: 674px; }
  .service-card {
    position: absolute; top: 0;
    width: 157px; height: 227px;
    border: 1px solid var(--card-border);
    text-align: center;
  }
  .service-icon {
    position: absolute; left: 53px; top: -25px;
    width: 50px; height: 50px; border-radius: 50%;
    background: var(--brand-blue);
    display: flex; align-items: center; justify-content: center;
  }
  .service-title {
    margin-top: 44px;
    font-family: "Roboto Slab", Georgia, serif;
    font-weight: 400; font-size: 15px; color: var(--ink);
  }
  .service-text {
    margin: 12px auto 0;
    width: 132px; height: 88px; overflow: hidden;
    font-size: 10.5px; line-height: 17.4px; color: var(--body-text);
  }
  .service-link {
    position: absolute; left: 0; right: 0; top: 189px;
    font-size: 10.5px; color: var(--brand-blue-text); text-decoration: none;
  }

  .section-rule {
    position: absolute; left: 0; top: 937px;
    width: 916px; height: 1px; background: var(--rule);
  }
  .intro { position: absolute; left: 0; top: 974px; width: 916px; text-align: center; }
  .intro-heading {
    font-family: "Roboto Slab", Georgia, serif;
    font-weight: 300; font-size: 26px; line-height: 34px;
    color: var(--brand-blue-text);
  }
  .intro-sub {
    margin-top: 8px;
    font-weight: 600; font-size: 17px; line-height: 24px; color: var(--ink);
    letter-spacing: 0.2px;
  }
  .intro-text { margin-top: 9px; font-size: 10.5px; color: var(--body-text); }
  .intro-text strong { color: var(--ink); font-weight: 600; }
  .star-divider { position: absolute; left: 374px; top: 1097px; }

  .footer-band {
    position: absolute; left: 0; top: 1174px;
    width: 916px; height: 26px; background: var(--footer-grey);
  }
</style>
</head>
<body>
<div class="page">
  <header class="site-header">
    <div class="brand">quorvane</div>
    <nav class="main-nav">
      <a class="is-current" style="left:248px">Home</a>
      <a style="left:309px">Who we are?</a>
      <a style="left:400px">What we do?</a>
      <a style="left:491px">Some of our Work</a>
      <a style="left:610px">Who we work with?</a>
      <a style="left:735px">Contact</a>
    </nav>
    <svg class="search-icon" width="13" height="13" viewBox="0 0 13 13" aria-label="Search">
      <circle cx="5.3" cy="5.3" r="4" fill="none" stroke="#fff" stroke-width="2"/>
      <line x1="8.3" y1="8.3" x2="12" y2="12" stroke="#fff" stroke-width="2.2" stroke-linecap="round"/>
    </svg>
  </header>

  <div class="hero" role="img" aria-label="Photo of two scientists in white lab coats working in a laboratory, one in goggles and mask using a wash bottle, the other reading a notebook"></div>

  <section class="services">
    <article class="service-card" style="left:0">
      <div class="service-icon">
        <svg width="20" height="22" viewBox="0 0 20 22"><rect x="3" y="2" width="14" height="18" rx="1.5" fill="none" stroke="#fff" stroke-width="2"/><line x1="6.5" y1="8" x2="13.5" y2="8" stroke="#fff" stroke-width="1.8"/><line x1="6.5" y1="12" x2="13.5" y2="12" stroke="#fff" stroke-width="1.8"/><line x1="6.5" y1="16" x2="11" y2="16" stroke="#fff" stroke-width="1.8"/></svg>
      </div>
      <h3 class="service-title">Promotion</h3>
      <p class="service-text">Quorvane can help you promote your brand – from the development of strategic communication campaigns to the creation of discrete..</p>
      <a class="service-link">Learn More</a>
    </article>
    <article class="service-card" style="left:186px">
      <div class="service-icon">
        <svg width="22" height="22" viewBox="0 0 22 22"><rect x="2" y="9" width="4" height="11" fill="#fff"/><path d="M7.5 9 L11 2.5 C12.5 2.5 13.5 3.5 13 5.5 L12.3 8.5 H18 C19.3 8.5 20 9.6 19.7 10.8 L18 18.5 C17.7 19.5 17 20 16 20 H7.5 Z" fill="#fff"/></svg>
      </div>
      <h3 class="service-title">Education</h3>
      <p class="service-text">Clinical papers, evidence summaries, scientific newsletters and accredited educational materials are among the supporting materials..</p>
      <a class="service-link">Learn More</a>
    </article>
    <article class="service-card" style="left:372px">
      <div class="service-icon">
        <svg width="22" height="18" viewBox="0 0 22 18"><rect x="4" y="2" width="14" height="10" rx="1" fill="none" stroke="#fff" stroke-width="1.8"/><path d="M1 14 H21 L19.5 16 H2.5 Z" fill="#fff"/></svg>
      </div>
      <h3 class="service-title">Programes</h3>
      <p class="service-text">From clinical audits to patient support activities, Quorvane has the experience to successfully develop and implement complex programs and activities.</p>
      <a class="service-link">Learn More</a>
    </article>
    <article class="service-card" style="left:558px">
      <div class="service-icon">
        <svg width="22" height="22" viewBox="0 0 24 24"><path d="M12 2 L14.9 8.6 L22 9.3 L16.6 14 L18.2 21 L12 17.3 L5.8 21 L7.4 14 L2 9.3 L9.1 8.6 Z" fill="#fff"/></svg>
      </div>
      <h3 class="service-title">Meetings</h3>
      <p class="service-text">You will maximise your investment in scientific meetings by employing Quorvane to manage the entire process from concept development to delivery on the day.</p>
      <a class="service-link">Learn More</a>
    </article>
  </section>

  <div class="section-rule"></div>

  <section class="intro">
    <h2 class="intro-heading">At Quorvane we are healthcare communication specialists;</h2>
    <p class="intro-sub">this means we’re scientists, journalists and marketers rolled into one.</p>
    <p class="intro-text">As you can see we provide all the things you’d expect from a top-class <strong>healthcare communications agency</strong>.</p>
  </section>

  <svg class="star-divider" width="216" height="16" viewBox="0 0 216 16" aria-hidden="true">
    <line x1="0" y1="8" x2="92" y2="8" stroke="#dcdcdc" stroke-width="1"/>
    <line x1="124" y1="8" x2="216" y2="8" stroke="#dcdcdc" stroke-width="1"/>
    <path d="M108 2 L109.8 6.2 L114.3 6.6 L110.9 9.6 L111.9 14 L108 11.7 L104.1 14 L105.1 9.6 L101.7 6.6 L106.2 6.2 Z" fill="#c9c9c9"/>
  </svg>

  <div class="footer-band"></div>
</div>
</body>
</html>
```